New web page design for our brand Casa Olmera

We have changed our logo and the image of our products, so we would like to redesign ,our web page as well according to the new design.
Our cosmetic products are based in nature and tradition, like they used to be prepared in the old pharmacies.
Our actual web is www.casaolmera.es, so we need similar estructure but completely different design.

Industry/Entity Type

Cosmetics

Number of Pages Required

5+ page

Requirements
Must have
• References to natural ingredients and also to old pharmacys or apothecaries.
Nice to have
• Nature images or old botanics drawings
• I would like to have a cover page with just an image saying welcome to Casa Olmera's world

```html
<!DOCTYPE html>
<html lang="es">
<head>
<meta charset="utf-8">
<title>Casa Olmera</title>
<link href="https://fonts.googleapis.com/css2?family=Open+Sans:wght@400;600;700&family=Kaushan+Script&display=swap" rel="stylesheet">
<style>
:root{
  --red:#8e1b1e;
  --red-dark:#6e1214;
  --cream:#f1ebde;
  --cream-2:#e4d9c3;
  --paper:#ffffff;
  --ink:#3a3a3a;
  --muted:#777;
  --line:#d9d2c4;
  --dark:#2b2b2b;
  --darker:#1e1e1e;
  --social:#2d7fc1;
}
*{box-sizing:border-box;margin:0;padding:0}
html,body{width:796px;height:1200px;overflow:hidden}
body{font-family:"Open Sans",Arial,sans-serif;color:var(--ink);background:var(--paper);position:relative;font-size:9px}
.topbar{height:44px;display:flex;align-items:center;justify-content:space-between;padding:0 54px;background:var(--paper)}
.follow{display:flex;align-items:center;gap:5px;font-size:9px;color:var(--muted);letter-spacing:.5px}
.dot{width:15px;height:15px;border-radius:50%;background:var(--social);display:inline-block}
.dot.red{background:#c0392b}
.phone{display:flex;align-items:center;gap:6px;color:var(--red);font-weight:700;font-size:12px}
.brand{position:absolute;left:50%;top:4px;transform:translateX(-50%);width:150px;height:88px;background:var(--paper);border:2px solid var(--red);border-radius:50%;display:flex;align-items:center;justify-content:center;z-index:3}
.brand span{font-family:"Open Sans",sans-serif;font-weight:700;font-size:17px;color:var(--red)}
.nav{height:34px;border-top:1px solid var(--line);border-bottom:1px solid var(--line);display:flex;align-items:center;justify-content:space-between;padding:0 54px;font-size:9px;font-weight:600;color:var(--red);letter-spacing:.4px}
.nav ul{display:flex;gap:26px;list-style:none}
.hero{height:252px;background:linear-gradient(#f4efe4,var(--cream));position:relative;display:flex;align-items:center;padding:0 54px}
.hero-img{width:350px;height:200px;border-radius:4px;background:radial-gradient(circle at 45% 50%,#3c4f86 0 18%,#e9e5dc 19% 100%)}
.hero-copy{margin-left:70px;width:260px}
.hero-copy h1{font-size:30px;font-weight:400;color:var(--dark);letter-spacing:1px;margin-bottom:8px}
.hero-copy h1 b{color:var(--red);font-weight:700}
.hero-copy p{font-size:9px;line-height:1.55;color:var(--muted);margin-bottom:14px}
.btn{display:inline-block;background:var(--red);color:#fff;font-weight:700;font-size:13px;padding:8px 14px;border-radius:3px}
.slides{position:absolute;bottom:6px;left:50%;transform:translateX(-50%);display:flex;gap:4px}
.slides i{width:26px;height:3px;background:#999;display:block}
.slides i:first-child{background:var(--dark)}
.section-title{font-family:"Kaushan Script",cursive;font-size:19px;color:var(--dark);display:flex;align-items:center;gap:10px}
.section-title::before,.section-title::after{content:"";flex:1;height:1px;background:#999}
.intro{display:flex;gap:40px;padding:18px 54px 0;height:184px}
.about{flex:1.2}
.about p{font-size:8.5px;line-height:1.6;color:var(--muted);margin-top:12px}
.about a{display:block;margin-top:6px;font-weight:700;color:var(--dark);font-size:8.5px}
.services{flex:1}
.svc-row{display:flex;justify-content:space-around;margin-top:20px;text-align:center;font-size:10px;color:var(--ink)}
.svc-ico{width:58px;height:58px;border-radius:50%;background:#444;margin:0 auto 8px;display:flex;align-items:center;justify-content:center}
.products{padding:0 54px}
.grid{display:grid;grid-template-columns:repeat(4,1fr);gap:14px 20px;margin-top:14px}
.card{height:150px;border:1px solid var(--line);padding:10px;display:flex;flex-direction:column;justify-content:space-between;position:relative}
.card h3{font-size:9.5px;font-weight:600;color:var(--dark);width:78px;line-height:1.25;position:relative;z-index:1}
.card .pic{position:absolute;right:10px;top:12px;width:56px;height:98px;border-radius:3px;background:linear-gradient(#ece8df,#c9bba4)}
.card .more{align-self:flex-start;background:var(--red-dark);color:#fff;font-size:6.5px;font-weight:700;padding:4px 7px}
.viewall{margin:14px auto 0;width:60px;text-align:center;border:1px solid var(--dark);font-size:6.5px;font-weight:700;padding:3px 0}
.perks{display:flex;gap:22px;padding:16px 54px 0}
.perk{flex:1;height:62px;background:var(--dark);color:#fff;display:flex;align-items:center;justify-content:center;gap:12px;font-size:10px;font-weight:700;letter-spacing:.5px;line-height:1.3}
.perk.gift{background:linear-gradient(#c99d7c,#b58467);color:#4a2c1a}
.footer{position:absolute;left:0;right:0;top:1008px;height:168px;background:var(--dark);color:#ccc;display:flex;gap:30px;padding:18px 54px}
.footer h4{font-family:"Kaushan Script",cursive;font-weight:400;font-size:13px;color:#fff;margin-bottom:10px}
.footer ul{list-style:none;line-height:1.9;font-size:8px}
.col1{width:150px}.col2{width:240px}.col3{flex:1}
.info{display:flex;gap:8px;align-items:flex-start;font-size:8px;line-height:1.5;margin-bottom:9px}
.field{height:22px;background:#fff;color:#999;font-size:8px;padding:5px 8px;margin-bottom:8px}
.sub{display:inline-block;background:#555;color:#fff;font-size:8px;font-weight:700;padding:5px 12px}
.legal{position:absolute;left:0;right:0;top:1176px;height:24px;background:var(--darker);display:flex;align-items:center;justify-content:space-between;padding:0 54px;font-size:7.5px;color:#aaa}
.legal .dots{display:flex;gap:4px}
.legal .dot{width:12px;height:12px;background:#555}
</style>
</head>
<body>
<header class="topbar">
  <div class="follow">FOLLOW US ON <span class="dot"></span><span class="dot"></span><span class="dot"></span><span class="dot red"></span></div>
  <div class="phone"><svg width="13" height="13" viewBox="0 0 24 24"><path fill="#8e1b1e" d="M6.6 10.8a15 15 0 0 0 6.6 6.6l2.2-2.2c.3-.3.7-.4 1-.2 1.1.4 2.3.6 3.6.6.6 0 1 .4 1 1V20c0 .6-.4 1-1 1A17 17 0 0 1 3 4c0-.6.4-1 1-1h3.5c.6 0 1 .4 1 1 0 1.3.2 2.5.6 3.6.1.3 0 .7-.2 1z"/></svg>555-204-3318</div>
</header>
<div class="brand"><span>Casa Olmera</span></div>
<nav class="nav">
  <ul><li>HOME</li><li>LABORATORY</li><li>PRODUCT LINES</li></ul>
  <ul><li>SERVICES</li><li>NEWS</li><li>SHOP</li><li>CONTACT</li></ul>
</nav>
<section class="hero">
  <div class="hero-img" role="img" aria-label="Photograph of the cosmetic product range in jars, tubes and bottles"></div>
  <div class="hero-copy">
    <h1><b>Casa</b> OLMERA</h1>
    <p>Natural care made the old apothecary way, with herbs, oils and honest recipes passed down in our laboratory for generations.</p>
    <span class="btn">SHOP NOW!</span>
  </div>
  <div class="slides"><i></i><i></i><i></i></div>
</section>
<section class="intro">
  <div class="about">
    <h2 class="section-title">About Casa Olmera</h2>
    <p>Our story began in a small town pharmacy where remedies were prepared by hand from plants, flowers and pure oils. Today we keep that spirit alive, blending natural ingredients with careful science to create gentle cosmetics for the whole family, made slowly and with respect for tradition.</p>
    <p>Every formula is tested in our own laboratory and crafted in small batches for quality you can feel.</p>
    <a>Read More</a>
  </div>
  <div class="services">
    <h2 class="section-title">Our Services</h2>
    <div class="svc-row">
      <div><div class="svc-ico"><svg width="26" height="26" viewBox="0 0 24 24"><circle cx="12" cy="8" r="4" fill="#fff"/><path d="M4 21c0-4 4-7 8-7s8 3 8 7z" fill="#fff"/></svg></div>Personalización</div>
      <div><div class="svc-ico"><svg width="26" height="26" viewBox="0 0 24 24"><circle cx="12" cy="12" r="6" fill="none" stroke="#fff" stroke-width="3"/><circle cx="12" cy="12" r="2" fill="#fff"/></svg></div>Fabricación A Terceros</div>
    </div>
  </div>
</section>
<section class="products">
  <h2 class="section-title">Our Products</h2>
  <div class="grid">
    <div class="card"><h3>Cuidados Naturales</h3><div class="pic" role="img" aria-label="Product photograph"></div><span class="more">READ MORE</span></div>
    <div class="card"><h3>Línea Recomendación Farmacéutica</h3><div class="pic" role="img" aria-label="Product photograph"></div><span class="more">READ MORE</span></div>
    <div class="card"><h3>Tratamiento Corporal</h3><div class="pic" role="img" aria-label="Product photograph"></div><span class="more">READ MORE</span></div>
    <div class="card"><h3>Higiene Familiar</h3><div class="pic" role="img" aria-label="Product photograph"></div><span class="more">READ MORE</span></div>
    <div class="card"><h3>Cuidados Naturales</h3><div class="pic" role="img" aria-label="Product photograph"></div><span class="more">READ MORE</span></div>
    <div class="card"><h3>Línea Aromática</h3><div class="pic" role="img" aria-label="Product photograph"></div><span class="more">READ MORE</span></div>
    <div class="card"><h3>Cosmética</h3><div class="pic" role="img" aria-label="Product photograph"></div><span class="more">READ MORE</span></div>
    <div class="card"><h3>Línea Geriátrica</h3><div class="pic" role="img" aria-label="Product photograph"></div><span class="more">READ MORE</span></div>
  </div>
  <div class="viewall">VIEW ALL</div>
</section>
<section class="perks">
  <div class="perk"><svg width="30" height="20" viewBox="0 0 30 20"><rect x="1" y="3" width="17" height="11" fill="none" stroke="#fff" stroke-width="2"/><path d="M18 7h6l4 4v3h-10z" fill="none" stroke="#fff" stroke-width="2"/><circle cx="7" cy="16" r="2.5" fill="#fff"/><circle cx="23" cy="16" r="2.5" fill="#fff"/></svg><span>ENJOY EVERYDAY<br>FREE SHIPPING</span></div>
  <div class="perk"><svg width="24" height="22" viewBox="0 0 24 22"><rect x="2" y="2" width="20" height="18" fill="none" stroke="#fff" stroke-width="2"/><path d="M12 2v18" stroke="#fff" stroke-width="2"/></svg><span>REQUEST A<br>FREE CATALOG</span></div>
  <div class="perk gift" role="img" aria-label="Patterned gift card banner"><span>E-GIFT<br>CARDS</span></div>
</section>
<footer class="footer">
  <div class="col1"><h4>Quick Links</h4><ul><li>Laboratorio</li><li>Línea de productos</li><li>Servicios</li><li>Noticias</li><li>Contacto</li><li>Tienda</li></ul></div>
  <div class="col2"><h4>Store Information</h4>
    <div class="info"><svg width="10" height="12" viewBox="0 0 24 24"><path fill="#ccc" d="M12 2a7 7 0 0 0-7 7c0 5 7 13 7 13s7-8 7-13a7 7 0 0 0-7-7zm0 9.5a2.5 2.5 0 1 1 0-5 2.5 2.5 0 0 1 0 5z"/></svg><span>C/ Alameda Vieja 14, Bajo B<br>28100 Villanueva del Campo · Madrid · España</span></div>
    <div class="info"><svg width="11" height="10" viewBox="0 0 24 20"><rect x="1" y="1" width="22" height="18" fill="none" stroke="#ccc" stroke-width="2"/><path d="M1 1l11 9 11-9" fill="none" stroke="#ccc" stroke-width="2"/></svg><span>hola@casaolmera.es</span></div>
    <div class="info"><svg width="10" height="10" viewBox="0 0 24 24"><path fill="#ccc" d="M6.6 10.8a15 15 0 0 0 6.6 6.6l2.2-2.2c.3-.3.7-.4 1-.2 1.1.4 2.3.6 3.6.6.6 0 1 .4 1 1V20c0 .6-.4 1-1 1A17 17 0 0 1 3 4c0-.6.4-1 1-1h3.5c.6 0 1 .4 1 1 0 1.3.2 2.5.6 3.6.1.3 0 .7-.2 1z"/></svg><span style="font-size:11px">+34 900 555 214</span></div>
  </div>
  <div class="col3"><h4>Sign Up For Newsletter</h4>
    <div class="field">Correo Electrónico</div>
    <div class="field">Nombre del contacto</div>
    <span class="sub">SUBSCRIBE</span>
  </div>
</footer>
<div class="legal"><span>© 2015 Casa Olmera. All Rights Reserved.</span><span class="dots"><span class="dot"></span><span class="dot"></span><span class="dot"></span><span class="dot"></span></span></div>
</body>
</html>
```